Web Design Project for a new download application :-)

We need a website design and a logo design for a new website and desktop application.
The Website will be www.Fetchora.com
The installed application will be: Fetchora

Fetchora is a desktop application that searches and finds all kind of Media files (Movies, Games, Songs, software, etc..)
Fetchora will also manage the download process for the selected files.
Fetchora automates the whole search and download process.

User Flow:
users will initially visit the website.
user will download the application from the website
user will install the application on his computer.
user will run and use the application.

What makes our software special:
-Great search engine for searching media files.
-Very high speed downloads. maximum speeds.
-Allow used to Search by: file type, size, date, format
-Pause and resume downloads
-Get any file you want instantly.
-Unlimited Downloads.

We will need:
Logo
WebSite Design
Icons for the desktop application.

we need only PSDs - no codded pages are needed !

Design to the following screen Size & resolution: 1024 x 768

Target Market(s)

movies and music lovers.
users who download movies, games, softwares, music etc...

Industry/Entity Type

Software

Requirements
Must have
• must have download button

Files

```html
<!DOCTYPE html>
<html lang="en">
<head>
<meta charset="utf-8">
<title>Fetchora — The Best in Business</title>
<link rel="stylesheet" href="https://fonts.googleapis.com/css2?family=Open+Sans:ital,wght@0,300;0,400;0,600;1,300;1,400&display=swap">
<style>
  :root {
    --brand-blue: #2a88b8;
    --brand-blue-dark: #1d6f99;
    --bar-top: #6fb7d6;
    --bar-bottom: #2b87b3;
    --ink: #3c3c3c;
    --ink-soft: #5a5a5a;
    --ink-muted: #777;
    --line: #d4d4d4;
    --panel-light: #f4f4f4;
    --panel-mid: #e6e6e6;
    --tile-top: #6cc0e6;
    --tile-bottom: #2a8fc4;
    --white: #ffffff;
  }
  * { box-sizing: border-box; margin: 0; padding: 0; }
  html, body { width: 1200px; height: 900px; overflow: hidden; background: var(--white); }
  body { font-family: "Open Sans", Arial, sans-serif; color: var(--ink); position: relative; }

  .site { position: relative; width: 1200px; height: 900px; overflow: hidden; background: var(--white); }

  /* Top bar */
  .topbar { position: absolute; left: 0; top: 0; width: 1200px; height: 64px;
    background: linear-gradient(to bottom, var(--bar-top), var(--bar-bottom)); }
  .topbar__url { position: absolute; left: 14px; top: 44px; font-size: 13px; letter-spacing: 1px; color: #0f2f45; }
  .topbar__lang { position: absolute; left: 1010px; top: 44px; font-size: 13px; letter-spacing: 1px; color: #0f2f45; }
  .topbar__lang span { margin-left: 12px; }
  .nav { position: absolute; top: 23px; left: 0; }
  .nav__tab { position: absolute; top: 0; width: 131px; height: 41px; border-radius: 9px 9px 0 0;
    background: linear-gradient(to bottom, #ffffff, #e4eef3); color: var(--brand-blue);
    font-size: 18px; text-align: center; line-height: 41px; box-shadow: 0 -1px 3px rgba(0,0,0,.15); }
  .nav__tab--support { font-style: italic; }

  /* Header */
  .hero-deco { position: absolute; left: 520px; top: 70px; width: 380px; height: 250px;
    background: radial-gradient(ellipse at center, #eef2f5 0%, rgba(255,255,255,0) 70%); }
  .logo { position: absolute; left: 60px; top: 86px; display: flex; align-items: center; gap: 14px; }
  .logo__dot { width: 40px; height: 40px; border-radius: 50%; background: #9fb8c8; }
  .logo__name { font-size: 50px; font-weight: 400; color: var(--brand-blue); line-height: 1; }
  .tagline { position: absolute; left: 205px; top: 148px; font-size: 22px; font-weight: 300; color: var(--ink-soft); }

  .benefits { position: absolute; left: 0; top: 193px; width: 580px; height: 150px;
    background: linear-gradient(to right, #ececec, #ffffff 85%);
    border-top: 1px solid var(--line); border-bottom: 1px solid var(--line); }
  .benefits__item { position: absolute; left: 48px; display: flex; gap: 14px; font-size: 15px; line-height: 17px; letter-spacing: .6px; color: var(--ink); }
  .benefits__item svg { flex: none; margin-top: 6px; }

  .preview { position: absolute; left: 582px; top: 144px; width: 282px; height: 235px; border-radius: 4px;
    background: linear-gradient(to bottom, #dfe3e6 0, #dfe3e6 8%, #2a7fb3 8%, #5fb0dc 45%, #f5f7f8 45%, #e8ecef 100%);
    box-shadow: 0 3px 8px rgba(0,0,0,.3); }

  .download-btn { position: absolute; left: 881px; top: 220px; width: 319px; height: 87px;
    border-radius: 10px 0 0 10px; border: 1px solid #cfd6da; border-right: none;
    background: linear-gradient(to bottom, #fafafa 0%, #eceeef 50%, #cfd8de 100%);
    font-size: 38px; font-weight: 300; color: #555; text-align: center; line-height: 85px; text-decoration: none; }
  .download-note { position: absolute; left: 934px; top: 324px; font-size: 22px; font-style: italic; font-weight: 300; color: var(--ink-soft); }

  .categories { position: absolute; left: 0; top: 405px; width: 1200px; height: 34px;
    background: linear-gradient(to bottom, #f7f7f7, #e8e8e8); border-top: 1px solid var(--line); border-bottom: 1px solid var(--line);
    font-size: 15px; color: var(--ink); text-align: center; line-height: 32px; padding-left: 175px; }

  /* Features */
  .features__title { position: absolute; left: 53px; top: 474px; font-size: 26px; letter-spacing: 1.5px; color: var(--brand-blue); font-weight: 400; }
  .features__list { position: absolute; left: 88px; top: 533px; list-style: none; }
  .features__item { display: flex; align-items: center; gap: 20px; height: 26px; font-size: 15px; letter-spacing: 1px; color: var(--ink-soft); }

  .people { position: absolute; left: 633px; top: 457px; width: 187px; height: 246px;
    background: linear-gradient(to bottom, #a8a8a8, #c8c8c8 60%, rgba(255,255,255,0)); border-radius: 40px 40px 0 0; opacity: .75; }
  .product-box { position: absolute; left: 914px; top: 445px; width: 246px; height: 293px;
    background: linear-gradient(135deg, #6fb2d8, #a9cfe3 55%, #7db2cf); box-shadow: 6px 10px 16px rgba(0,0,0,.25); }

  /* Bottom */
  .services { position: absolute; left: 0; top: 712px; width: 1200px; height: 188px;
    background: linear-gradient(to bottom, #ededed, #d6d6d6); }
  .service { position: absolute; top: 0; width: 300px; height: 188px; }
  .service + .service { border-left: 1px solid #c9c9c9; }
  .service__icon { position: absolute; left: 18px; top: 52px; width: 93px; height: 84px; border-radius: 8px;
    border: 3px solid #e9f4fa; background: linear-gradient(to bottom, var(--tile-top), var(--tile-bottom));
    box-shadow: 0 2px 4px rgba(0,0,0,.25); display: flex; align-items: center; justify-content: center; }
  .service__title { position: absolute; left: 128px; top: 62px; font-size: 15px; letter-spacing: 1px; color: var(--brand-blue); font-weight: 400; text-transform: uppercase; }
  .service__title--plain { text-transform: none; }
  .service__text { position: absolute; left: 128px; top: 82px; font-size: 13px; line-height: 17px; letter-spacing: .8px; color: var(--ink); width: 170px; }
</style>
</head>
<body>
<div class="site">

  <header class="topbar">
    <div class="topbar__url">www.Fetchora.com</div>
    <nav class="nav">
      <a class="nav__tab" style="left:390px">Home</a>
      <a class="nav__tab" style="left:543px">Download</a>
      <a class="nav__tab nav__tab--support" style="left:696px">Support</a>
      <a class="nav__tab" style="left:847px">Affiliates</a>
    </nav>
    <div class="topbar__lang">Language<span>English ▾</span></div>
  </header>

  <div class="hero-deco" role="img" aria-label="Faint floral ornament behind the header"></div>

  <div class="logo">
    <span class="logo__dot"></span>
    <span class="logo__name">Fetchora</span>
  </div>
  <div class="tagline">The Best in Business</div>

  <section class="benefits">
    <div class="benefits__item" style="top:14px">
      <svg width="24" height="20" viewBox="0 0 24 20"><path d="M2 11 L9 17 L22 2" fill="none" stroke="#2a88b8" stroke-width="3.5" stroke-linecap="round" stroke-linejoin="round"/></svg>
      <p>Fetchora is a desktop application that searches and finds all<br>kind of Media files (Movies, Games, Songs, software, etc..)</p>
    </div>
    <div class="benefits__item" style="top:63px">
      <svg width="24" height="20" viewBox="0 0 24 20"><path d="M2 11 L9 17 L22 2" fill="none" stroke="#2a88b8" stroke-width="3.5" stroke-linecap="round" stroke-linejoin="round"/></svg>
      <p>Fetchora will also manage the download process<br>for the selected files.</p>
    </div>
    <div class="benefits__item" style="top:112px">
      <svg width="24" height="20" viewBox="0 0 24 20"><path d="M2 11 L9 17 L22 2" fill="none" stroke="#2a88b8" stroke-width="3.5" stroke-linecap="round" stroke-linejoin="round"/></svg>
      <p>Fetchora automates the whole search and<br>download process.</p>
    </div>
  </section>

  <div class="preview" role="img" aria-label="Browser window showing a screenshot of a sample website"></div>

  <a class="download-btn">Download Now</a>
  <div class="download-note">Download, Install &amp; Use</div>

  <div class="categories">Movies, Music, Songs, Softwares, Games, Documenteries, Presentations, Tutorials, Mobile....</div>

  <h2 class="features__title">What makes our software special ?</h2>
  <ul class="features__list">
    <li class="features__item"><svg width="17" height="14" viewBox="0 0 17 14"><path d="M0 0 L17 7 L0 14 L5 7 Z" fill="#2a88b8"/></svg>Great search engine for searching media files.</li>
    <li class="features__item"><svg width="17" height="14" viewBox="0 0 17 14"><path d="M0 0 L17 7 L0 14 L5 7 Z" fill="#2a88b8"/></svg>Very high speed downloads. maximum speeds.</li>
    <li class="features__item"><svg width="17" height="14" viewBox="0 0 17 14"><path d="M0 0 L17 7 L0 14 L5 7 Z" fill="#2a88b8"/></svg>Allow used to Search by: file type, size, date, format</li>
    <li class="features__item"><svg width="17" height="14" viewBox="0 0 17 14"><path d="M0 0 L17 7 L0 14 L5 7 Z" fill="#2a88b8"/></svg>Pause and resume downloads</li>
    <li class="features__item"><svg width="17" height="14" viewBox="0 0 17 14"><path d="M0 0 L17 7 L0 14 L5 7 Z" fill="#2a88b8"/></svg>Get any file you want instantly.</li>
    <li class="features__item"><svg width="17" height="14" viewBox="0 0 17 14"><path d="M0 0 L17 7 L0 14 L5 7 Z" fill="#2a88b8"/></svg>Unlimited Downloads.</li>
  </ul>

  <div class="people" role="img" aria-label="Grey silhouettes of two business people shaking hands"></div>
  <div class="product-box" role="img" aria-label="Blue software product box with a Buy Now badge"></div>

  <section class="services">
    <div class="service" style="left:0">
      <div class="service__icon" role="img" aria-label="Film strip icon"></div>
      <h3 class="service__title">Media</h3>
      <p class="service__text">Media, Softwares, Games, Documentaries, Presentations...</p>
    </div>
    <div class="service" style="left:300px">
      <div class="service__icon" role="img" aria-label="Film reel icon"></div>
      <h3 class="service__title">Video Tour</h3>
      <p class="service__text">Take a Tour for help and guidance</p>
    </div>
    <div class="service" style="left:600px">
      <div class="service__icon">
        <svg width="64" height="64" viewBox="0 0 64 64"><circle cx="40" cy="22" r="13" fill="none" stroke="#eaf6fc" stroke-width="4"/><line x1="31" y1="31" x2="10" y2="54" stroke="#eaf6fc" stroke-width="6" stroke-linecap="round"/></svg>
      </div>
      <h3 class="service__title">Search Engine</h3>
      <p class="service__text">Great search engine specifically beneficial for Music Lovers...</p>
    </div>
    <div class="service" style="left:900px">
      <div class="service__icon" role="img" aria-label="Circular arrows icon"></div>
      <h3 class="service__title service__title--plain">Download Manager</h3>
      <p class="service__text" style="width:168px">High speed downloads are possible by different search types e.g. Date...</p>
    </div>
  </section>

</div>
</body>
</html>
```